TranquilPathbyHolt.com

I am looking to advertise our new business offering, tranquilpathbyholt.com, to our local hospice, nursing homes and hospitals. The idea was to have a nice, straightforward colorful postcard with a logo on the front and information on the back. Please peruse the site and utilize any information necessary to convey our concept. Here are the bullet points I'd like on the back of the card:

Tranquil Path by Holt is a cost-effective cremation offering that allows families to arrange for disposition of their loved one in the comfort of their own home.Our promise to you:

1) Your loved one will be transferred into the care of our funeral home with the utmost dignity and respect by the Holt staff. Upon arrival to our facility, they will never leave our care.

2) A trained director will contact the family, via phone, to assist with any questions or concerns.

3) By accessing www.tranquilpathbyholt.com, our intuitive site will take you step-by-step through the cremation arrangement process.

4) A positive identification will be made by the family prior to the cremation process. This will be done securely through our tranquilpathbyholt.com site.

Target Market(s)

Residents of Haywood County needing a low-cost disposition via cremation.

Industry/Entity Type

Business

Font styles to use
Serif

Colors

Designer to choose colors to be used in the design.

Requirements
Must have
• Tasteful design, somewhat of a serene front with a simple logo. The bullet points on the back.
Nice to have
• I have never designed a postcard so I'm relying on a professional to put the must haves.
Should not have
• I'm not looking to place our price on the brochure.

```html
<!DOCTYPE html>
<html lang="en">
<head>
<meta charset="utf-8">
<title>Tranquil Path by Holt – Postcard</title>
<link rel="stylesheet" href="https://fonts.googleapis.com/css2?family=Roboto+Slab:wght@400;700&family=Noto+Serif:wght@400;700&family=Tinos:wght@400;700&display=swap">
<style>
  :root {
    --backdrop: #3b3b3b;
    --paper: #ffffff;
    --panel-grey: #e9eaec;
    --leaf: #7dc242;
    --forest: #1e7a2e;
    --deep-green: #0f5a22;
    --navy: #1d3f78;
    --blue-text: #2a5ea8;
    --ink: #1e1e1e;
    --band: #d3dcef;
    --rule: #d4d4d4;
  }
  * { box-sizing: border-box; margin: 0; padding: 0; }
  html, body { width: 1200px; height: 2479px; overflow: hidden; }
  body { background: var(--backdrop); position: relative; font-family: "Noto Serif", Georgia, serif; }

  .card { position: absolute; left: 114px; width: 972px; height: 648px; background: var(--paper); overflow: hidden; box-shadow: 0 4px 14px rgba(0,0,0,.45); }
  .card--back { top: 564px; }
  .card--front { top: 1267px; }

  .card__art { position: absolute; inset: 0; width: 100%; height: 100%; }

  /* back side */
  .brand { position: absolute; left: 32px; top: 28px; display: flex; align-items: center; gap: 18px; }
  .brand__mark { width: 62px; height: 62px; background: var(--ink); }
  .brand__name { font-family: "Tinos", serif; font-weight: 700; color: var(--ink); line-height: 1.05; }
  .brand__name .big { display: block; font-size: 50px; letter-spacing: 1px; }
  .brand__name .small { display: block; font-size: 19px; }

  .intro { position: absolute; left: 32px; top: 146px; width: 500px; font-weight: 700; font-size: 16px; line-height: 1.3; color: var(--forest); }
  .promises { position: absolute; left: 32px; top: 232px; width: 490px; list-style: none; }
  .promises li { font-size: 13.5px; line-height: 1.38; color: var(--ink); margin-bottom: 8px; padding-left: 26px; position: relative; }
  .promises li span.accent { color: var(--blue-text); }
  .promises li svg { position: absolute; left: 0; top: 4px; width: 18px; height: 12px; }

  .touch { position: absolute; left: 0; top: 482px; width: 560px; height: 60px; background: var(--band); padding: 5px 0 0 46px; }
  .touch__title { font-weight: 700; font-size: 15.5px; color: var(--deep-green); }
  .touch__text { font-size: 13.5px; line-height: 1.35; color: var(--ink); }

  .contact { position: absolute; left: 28px; font-size: 16px; color: var(--ink); display: flex; align-items: center; gap: 10px; }
  .contact--name { top: 556px; font-weight: 700; font-size: 15px; color: var(--deep-green); }
  .contact--phone { top: 583px; font-weight: 700; font-size: 18px; color: var(--deep-green); }
  .contact--web { top: 613px; }
  .contact svg { width: 20px; height: 20px; }

  .stamp { position: absolute; left: 740px; top: 78px; width: 92px; height: 104px; border: 1.5px solid var(--rule); }
  .address-line { position: absolute; left: 735px; width: 205px; height: 0; border-top: 1.5px solid var(--rule); }

  /* front side */
  .photo { position: absolute; left: 0; top: 0; width: 972px; height: 500px;
    background: radial-gradient(ellipse at 72% 42%, #8a6a4a 0 12%, transparent 26%),
                radial-gradient(ellipse at 30% 30%, #6aa33e, transparent 60%),
                linear-gradient(160deg, #3f8a2c, #2f6f22 55%, #4f9a33); }
  .headline { position: absolute; left: 50px; top: 78px; font-family: "Roboto Slab", serif; font-weight: 700; font-size: 58px; line-height: 1.14; color: #fff; letter-spacing: 1px; text-shadow: 0 2px 4px rgba(0,0,0,.3); }

  .lockup { position: absolute; left: 58px; top: 490px; display: flex; align-items: center; gap: 16px; }
  .lockup__mark { width: 58px; height: 58px; background: var(--navy); }
  .lockup__name { font-family: "Tinos", serif; font-size: 44px; color: var(--navy); }
  .tagline { position: absolute; left: 238px; top: 572px; font-family: "Tinos", serif; font-size: 21px; color: var(--navy); }

  .front-contact { position: absolute; right: 68px; top: 510px; text-align: right; font-family: "Noto Serif", serif; }
  .front-contact__title { display: inline-block; font-weight: 700; font-size: 19px; color: var(--navy); border-bottom: 2px solid var(--navy); padding-bottom: 1px; }
  .front-contact__row { display: flex; align-items: center; justify-content: flex-end; gap: 10px; margin-top: 12px; font-size: 20px; color: var(--ink); }
  .front-contact__row.phone { font-weight: 700; color: var(--deep-green); }
  .front-contact__row svg { width: 20px; height: 20px; }
</style>
</head>
<body>

<section class="card card--back">
  <svg class="card__art" viewBox="0 0 972 648" preserveAspectRatio="none" aria-hidden="true">
    <defs>
      <linearGradient id="panelShade" x1="0" y1="0" x2="1" y2="1">
        <stop offset="0" stop-color="#ffffff"/>
        <stop offset=".45" stop-color="#eceef0"/>
        <stop offset="1" stop-color="#f7f7f8"/>
      </linearGradient>
    </defs>
    <path d="M0 0 H455 C575 70 520 420 540 648 H0 Z" fill="url(#panelShade)"/>
    <path d="M455 0 C575 70 520 420 540 648" fill="none" stroke="var(--leaf)" stroke-width="14"/>
    <path d="M470 0 C585 80 535 420 556 648" fill="none" stroke="var(--forest)" stroke-width="3"/>
  </svg>

  <div class="brand">
    <div class="brand__mark"></div>
    <div class="brand__name"><span class="big">HOLT</span><span class="small">FUNERAL HOMES, INC. &amp; CREMATION SERVICES</span></div>
  </div>

  <p class="intro">Tranquil Path by Holt is a cost-effective cremation offering that allows families to arrange for disposition of their loved one in the comfort of their own home.Our promise to you:</p>

  <ul class="promises">
    <li><svg viewBox="0 0 18 12"><path d="M1 6 H15 M10 1 L16 6 L10 11" fill="none" stroke="var(--forest)" stroke-width="1.6"/></svg>Your loved one will be transferred into the care of our funeral home with the utmost dignity and respect by the Holt staff. Upon arrival to our facility, they will never leave our care.</li>
    <li><svg viewBox="0 0 18 12"><path d="M1 6 H15 M10 1 L16 6 L10 11" fill="none" stroke="var(--forest)" stroke-width="1.6"/></svg><span class="accent">A trained director will contact the family, via phone, to assist with any questions or concerns.</span></li>
    <li><svg viewBox="0 0 18 12"><path d="M1 6 H15 M10 1 L16 6 L10 11" fill="none" stroke="var(--forest)" stroke-width="1.6"/></svg>By accessing www.tranquilpathbyholt.com, our intuitive site will take you step-by-step through the cremation arrangement process.</li>
    <li><svg viewBox="0 0 18 12"><path d="M1 6 H15 M10 1 L16 6 L10 11" fill="none" stroke="var(--forest)" stroke-width="1.6"/></svg><span class="accent">A positive identification will be made by the family prior to the cremation process. This will be done securely through our tranquilpathbyholt.com site.</span></li>
  </ul>

  <div class="touch">
    <p class="touch__title">Get in Touch</p>
    <p class="touch__text">Feel free to contact us with any question, comments,<br>or inquiries, and we will reply as soon as possible.</p>
  </div>

  <p class="contact contact--name">Tranquil Path by Holt</p>
  <p class="contact contact--phone">
    <svg viewBox="0 0 20 20"><circle cx="10" cy="10" r="9" fill="none" stroke="var(--deep-green)" stroke-width="1.6"/><path d="M7 5.5 L8.6 8 L7.6 9 C8.3 10.6 9.4 11.7 11 12.4 L12 11.4 L14.5 13 L13.5 14.5 C9.5 14 6 10.5 5.5 6.5 Z" fill="var(--deep-green)"/></svg>
    (828) 555-0142
  </p>
  <p class="contact contact--web">
    <svg viewBox="0 0 20 20"><circle cx="10" cy="10" r="8" fill="none" stroke="var(--deep-green)" stroke-width="1.5"/><ellipse cx="10" cy="10" rx="3.5" ry="8" fill="none" stroke="var(--deep-green)" stroke-width="1.3"/><path d="M2 10 H18" stroke="var(--deep-green)" stroke-width="1.3"/></svg>
    www.tranquilpathbyholt.com
  </p>

  <div class="stamp"></div>
  <div class="address-line" style="top:268px"></div>
  <div class="address-line" style="top:304px"></div>
</section>

<section class="card card--front">
  <div class="photo" role="img" aria-label="Photo of cupped hands holding soil with a young green seedling, against a soft green background"></div>
  <svg class="card__art" viewBox="0 0 972 648" preserveAspectRatio="none" aria-hidden="true">
    <path d="M0 420 C260 360 560 360 972 330 V380 C600 400 300 410 0 470 Z" fill="var(--leaf)"/>
    <path d="M0 440 C280 380 600 385 972 360 V648 H0 Z" fill="var(--forest)"/>
    <path d="M0 470 C300 415 620 410 972 385 V648 H0 Z" fill="var(--paper)"/>
    <path d="M0 470 C300 415 620 410 972 385" fill="none" stroke="var(--leaf)" stroke-width="3"/>
  </svg>

  <h1 class="headline">CARING<br>FOR THE<br>DEPARTED!</h1>

  <div class="lockup">
    <div class="lockup__mark"></div>
    <span class="lockup__name">Tranquil Path by Holt</span>
  </div>
  <p class="tagline">The Best for Less</p>

  <div class="front-contact">
    <p class="front-contact__title">contact us</p>
    <p class="front-contact__row phone">
      <svg viewBox="0 0 20 20"><circle cx="10" cy="10" r="9" fill="none" stroke="var(--deep-green)" stroke-width="1.6"/><path d="M7 5.5 L8.6 8 L7.6 9 C8.3 10.6 9.4 11.7 11 12.4 L12 11.4 L14.5 13 L13.5 14.5 C9.5 14 6 10.5 5.5 6.5 Z" fill="var(--deep-green)"/></svg>
      (828) 555-0142
    </p>
    <p class="front-contact__row">
      <svg viewBox="0 0 20 20"><circle cx="10" cy="10" r="8" fill="none" stroke="var(--deep-green)" stroke-width="1.5"/><ellipse cx="10" cy="10" rx="3.5" ry="8" fill="none" stroke="var(--deep-green)" stroke-width="1.3"/><path d="M2 10 H18" stroke="var(--deep-green)" stroke-width="1.3"/></svg>
      www.tranquilpathbyholt.com
    </p>
  </div>
</section>

</body>
</html>
```